Action Jacket 8.5 X 11 double pocket folder requiring action

This folder will be mailed to a prospect when telephonically requested by the prospect.

It will have our logo on the front cover with a "tagline" marketing the attendant service on the front page in the space below the logo.

Tag line: Castavo Turns Turmoil Into Calm Before Repossession

Saving Foreclosure victims with the Short-Sale one at time with proven results.

The back cover can be used.

Further points:

Castavo primarily does Short-Sales
The Seller pays nothing.
THE SELLER PAYS NOTHING!!
Castavo pays the attorneys that negotiate on behalf of the Seller.
Negotiations are always done by highly specialized attorneys/paralegals.
Castavo is a word from Leviticus in the Old Testament. It means "Forgiveness of debt, return of property to its rightful owner and freeing of the slaves."

Seller expectations:
1. 3 to 6 extra months in your home; save rent.
2. Guaranteed "Waiver of Deficiency"
3. Almost all Castavo Sellers will attain a minimum of $3,000 relocation allowance, many are now receiving $10,000.
4. FORECLOSUE eliminated from the Credit Report

Target Market(s)

The prospect has already responded to a mail piece and agreed telephonically to List their home. This piece is designed to re-enforce their decision and memorialize their decision on paper.
This piece will be a response mailer being sent OVERNIGHT with forms to sign and return in a provided postage-paid OVERNIGHT return envelope. These are people facing the ANXIETY of the unknown having their homes auctioned at the end of a multi-year ordeal of foreclosure. They have many unanswered questions many of which cannot be answered at this time. This piece must be designed to emphasise and overcome their natural tendancy to hesitate. They all face an AUCTION DATE and time is of the essence. We have lost many clients due to their inability to make a decision and/or ambivalence. They then lose their homes while staring into the headlights like a deer.

Font styles to use
Serif
Other font styles liked:
• See Castavo Logo font

Requirements
Must have
• Short to the point message/s
• Crisp design
• Action demanding content
Should not have
• clutter

```html
<!DOCTYPE html>
<html lang="en">
<head>
<meta charset="utf-8">
<title>Castavo Real Estate Corporation – Pocket Folder</title>
<link href="https://fonts.googleapis.com/css2?family=Libre+Baskerville:ital,wght@0,400;0,700;1,400&family=Montserrat:wght@400;500&display=swap" rel="stylesheet">
<style>
  :root {
    --navy: #1c3f72;
    --navy-deep: #17335e;
    --gold: #e8a825;
    --paper: #ffffff;
    --paper-shade: #eeeeef;
    --stage: #e4e4e6;
    --sky-top: #c9c6c4;
    --sky-mid: #e2e0de;
    --house-tone: #a9a6a4;
    --ink-light: #ffffff;
  }
  * { box-sizing: border-box; margin: 0; padding: 0; }
  html, body { width: 850px; height: 1200px; overflow: hidden; }
  body {
    background: var(--stage);
    font-family: "Libre Baskerville", Georgia, serif;
    position: relative;
  }
  .spread {
    position: absolute;
    left: 25px;
    width: 800px;
    height: 518px;
    display: flex;
    box-shadow: 0 10px 28px rgba(0,0,0,0.18);
  }
  .spread--outside { top: 40px; }
  .spread--inside { top: 630px; }
  .panel { position: relative; width: 400px; height: 518px; overflow: hidden; }

  /* Back cover */
  .back-cover { background: var(--navy); color: var(--ink-light); padding: 56px 36px 0 40px; }
  .brand { display: flex; align-items: center; gap: 9px; }
  .brand-dot { width: 14px; height: 14px; border-radius: 50%; background: var(--gold); flex: none; }
  .brand-name { font-weight: 700; font-size: 30px; line-height: 1; letter-spacing: 0.2px; }
  .brand-sub { font-size: 10.5px; margin: 4px 0 0 23px; }
  .back-cover .brand-name, .back-cover .brand-sub { color: var(--ink-light); }
  .points { margin-top: 22px; font-size: 7.6px; line-height: 1.55; }
  .points p { margin: 0; }
  .expect-title { color: var(--gold); font-weight: 700; font-size: 10px; margin-top: 12px; }
  .expect-list { margin: 4px 0 0 22px; font-size: 7.6px; line-height: 1.55; }
  .contact { position: absolute; left: 40px; bottom: 52px; font-family: "Montserrat", Arial, sans-serif; font-size: 8.5px; line-height: 1.4; }
  .contact li { list-style: none; margin-top: 8px; position: relative; padding-left: 10px; }
  .contact li::before { content: ""; position: absolute; left: 0; top: 4px; width: 4px; height: 4px; border-radius: 50%; background: var(--gold); }

  /* Front cover */
  .front-cover { background: var(--sky-mid); }
  .cover-photo { position: absolute; inset: 0; background: linear-gradient(180deg, var(--sky-top) 0%, var(--sky-mid) 38%, var(--house-tone) 100%); }
  .front-brand { position: absolute; top: 42px; left: 0; right: 0; display: flex; flex-direction: column; align-items: center; }
  .front-brand .brand-name, .front-brand .brand-sub { color: var(--navy); }
  .tagline { margin-top: 22px; color: var(--navy-deep); font-size: 10px; line-height: 1.45; text-align: center; width: 230px; }
  .web-band { position: absolute; right: 0; bottom: 66px; width: 215px; height: 16px; background: var(--navy); color: var(--ink-light); font-family: "Montserrat", Arial, sans-serif; font-size: 8.5px; letter-spacing: 1.4px; line-height: 16px; padding-left: 16px; }

  /* Inside spread */
  .inside-left { background: linear-gradient(90deg, var(--paper) 0%, var(--paper-shade) 100%); }
  .inside-right { background: linear-gradient(90deg, var(--paper-shade) 0%, var(--paper) 18%); }
  .pocket { position: absolute; left: 0; bottom: 0; width: 400px; height: 220px; }
  .pocket-brand { position: absolute; right: 58px; bottom: 92px; }
  .pocket-brand .brand-name, .pocket-brand .brand-sub { color: var(--ink-light); }
</style>
</head>
<body>
  <section class="spread spread--outside">
    <article class="panel back-cover">
      <div class="brand"><span class="brand-dot"></span><span class="brand-name">Castavo</span></div>
      <div class="brand-sub">Real Estate Corporation</div>
      <div class="points">
        <p>Castavo primarily does Short-Sales</p>
        <p>The Seller pays nothing.</p>
        <p>THE SELLER PAYS NOTHING!!</p>
        <p>Castavo pays the attorneys that negotiate on behalf of the Seller.</p>
        <p>Negotiations are always done by highly specialized attorneys/paralegals.</p>
        <p>Castavo is a word from Leviticus in the Old Testament. It means "Forgiveness of debt, return of property to its rightful owner and freeing of the slaves."</p>
      </div>
      <h3 class="expect-title">Seller expectations:</h3>
      <ol class="expect-list">
        <li>3 to 6 extra months in your home; save rent.</li>
        <li>Guaranteed "Waiver of Deficiency"</li>
        <li>Almost all Castavo Sellers will attain a minimum of $3,000 relocation allowance, many are now receiving $10,000.</li>
        <li>FORECLOSURE eliminated from the Credit Report</li>
      </ol>
      <ul class="contact">
        <li>Castavo Real Estate Corporation<br>Dale Vernon Licensed Real Estate Broker</li>
        <li>Castavo Management Centre<br>1840 Marlow Avenue Brightwater, FL 34010</li>
      </ul>
    </article>
    <article class="panel front-cover">
      <div class="cover-photo" role="img" aria-label="Photograph of a two-storey suburban house with white siding and a front porch under a cloudy grey sky"></div>
      <div class="front-brand">
        <div class="brand"><span class="brand-dot"></span><span class="brand-name">Castavo</span></div>
        <div class="brand-sub">Real Estate Corporation</div>
        <p class="tagline">Castavo Turns Turmoil Into Calm Before Repossession</p>
      </div>
      <div class="web-band">www.CastavoREC.com</div>
    </article>
  </section>

  <section class="spread spread--inside">
    <article class="panel inside-left"></article>
    <article class="panel inside-right">
      <svg class="pocket" viewBox="0 0 400 220" aria-hidden="true">
        <path d="M22 0 H400 V220 H0 V28 Q0 0 22 0 Z" fill="var(--navy)"/>
      </svg>
      <div class="pocket-brand">
        <div class="brand"><span class="brand-dot"></span><span class="brand-name">Castavo</span></div>
        <div class="brand-sub">Real Estate Corporation</div>
      </div>
    </article>
  </section>
</body>
</html>
```